Boat and Caravan indoor/ outdoor storage

A new company that provides 4star indoor and outdoor storage for Boats and Caravans
Industry/Entity Type
It Company

```html
<!DOCTYPE html>
<html lang="en">
<head>
<meta charset="utf-8">
<title>Storage Flyer</title>
<link rel="stylesheet" href="https://fonts.googleapis.com/css2?family=Open+Sans:wght@400;600;700;800&display=swap">
<style>
  :root {
    --wine: #7c1522;
    --wine-deep: #5a0d17;
    --wine-light: #9c2231;
    --ink: #3a3a3a;
    --muted: #6b6b6b;
    --paper: #ffffff;
    --silver: #dcdcdc;
    --footer: #241a1b;
  }
  * { margin: 0; padding: 0; box-sizing: border-box; }
  html, body { width: 900px; height: 1200px; overflow: hidden; background: #f2f2f2; }
  body { font-family: "Open Sans", Arial, sans-serif; color: var(--ink); }
  .flyer { position: relative; width: 900px; height: 1200px; background: var(--paper); overflow: hidden; }
  .hero-photo {
    position: absolute; left: 0; top: 0; width: 900px; height: 620px;
    background: linear-gradient(180deg, #b9d3ea 0%, #dfe9f1 35%, #cfd3cf 52%, #c9b79a 75%, #b8a283 100%);
  }
  .shapes { position: absolute; inset: 0; width: 900px; height: 1200px; }
  .brand {
    position: absolute; left: 44px; top: 42px; color: var(--paper);
    font-weight: 700; font-size: 30px; line-height: 1.15; letter-spacing: 0.5px;
  }
  .headline {
    position: absolute; left: 48px; top: 628px; color: var(--paper);
    font-weight: 800; font-size: 60px; line-height: 1.1; letter-spacing: 0.5px;
  }
  .column { position: absolute; top: 812px; }
  .column.about { left: 48px; width: 372px; }
  .column.services { left: 478px; width: 380px; }
  .column h2 {
    color: var(--wine); font-size: 24px; font-weight: 800; letter-spacing: 0.5px;
    padding-bottom: 8px; margin-bottom: 14px; border-bottom: 2px solid var(--silver);
  }
  .column p { font-size: 15px; line-height: 1.55; color: var(--muted); margin-bottom: 12px; }
  .service-list { list-style: none; }
  .service-list li {
    display: flex; gap: 10px; align-items: flex-start;
    font-size: 15px; line-height: 1.5; color: var(--muted); margin-bottom: 10px;
  }
  .service-list svg { flex: 0 0 16px; margin-top: 4px; }
  .contact {
    position: absolute; right: 48px; top: 1112px; text-align: right; color: var(--paper);
  }
  .contact-line { display: flex; align-items: center; justify-content: flex-end; gap: 10px; font-size: 16px; font-weight: 600; }
  .contact-line .divider { color: var(--wine-light); }
  .website { margin-top: 12px; font-size: 20px; font-weight: 700; display: flex; align-items: center; justify-content: flex-end; gap: 10px; }
  .website::after { content: ""; width: 10px; height: 10px; background: var(--wine-light); border-radius: 50%; }
</style>
</head>
<body>
<main class="flyer">
  <div class="hero-photo" role="img" aria-label="Photo of a white motorhome towing a motorboat on a trailer, parked on a gravel lot under a blue sky"></div>

  <svg class="shapes" viewBox="0 0 900 1200" aria-hidden="true">
    <defs>
      <linearGradient id="bandFill" x1="0" y1="0" x2="1" y2="0">
        <stop offset="0" stop-color="#5a0d17"/>
        <stop offset="0.6" stop-color="#7c1522"/>
        <stop offset="1" stop-color="#9c2231"/>
      </linearGradient>
    </defs>
    <!-- header tab -->
    <path d="M0 0 H448 C492 0 500 34 488 68 C470 120 392 166 300 166 H0 Z" fill="#dcdcdc"/>
    <path d="M0 0 H430 C470 0 478 30 468 60 C452 108 380 150 296 150 H0 Z" fill="#7c1522"/>
    <!-- headline band -->
    <path d="M0 566 C260 552 600 512 900 424 V452 C600 536 260 578 0 590 Z" fill="#e8e8e8"/>
    <path d="M0 590 C260 578 600 536 900 452 V760 C650 770 320 790 0 790 Z" fill="url(#bandFill)"/>
    <path d="M0 790 C320 790 650 770 900 760 V790 C650 796 320 806 0 806 Z" fill="#ffffff"/>
    <!-- footer -->
    <path d="M0 1092 C300 1090 620 1078 900 1056 V1200 H0 Z" fill="#7c1522"/>
    <path d="M0 1100 C300 1098 620 1086 900 1066 V1200 H0 Z" fill="#241a1b"/>
  </svg>

  <div class="brand">COMPANY<br>NAME</div>

  <h1 class="headline">LOREM IPSUM DOLOR<br>SIT AMET</h1>

  <section class="column about">
    <h2>ABOUT US</h2>
    <p>Our storage site keeps your boat or caravan safe, dry and ready for the road or water. Covered bays, secure gates and daily checks give owners real peace of mind through every season of the year.</p>
    <p>We offer indoor and outdoor spaces in many sizes, with easy access and friendly staff on hand to help you move your vehicle in and out.</p>
  </section>

  <section class="column services">
    <h2>OUR SERVICE</h2>
    <ul class="service-list">
      <li><svg width="16" height="16" viewBox="0 0 16 16"><circle cx="8" cy="8" r="8" fill="#7c1522"/><path d="M4.5 8.3 L7 10.6 L11.6 5.6" stroke="#fff" stroke-width="1.8" fill="none"/></svg>Indoor caravan storage bays</li>
      <li><svg width="16" height="16" viewBox="0 0 16 16"><circle cx="8" cy="8" r="8" fill="#7c1522"/><path d="M4.5 8.3 L7 10.6 L11.6 5.6" stroke="#fff" stroke-width="1.8" fill="none"/></svg>Outdoor boat parking</li>
      <li><svg width="16" height="16" viewBox="0 0 16 16"><circle cx="8" cy="8" r="8" fill="#7c1522"/><path d="M4.5 8.3 L7 10.6 L11.6 5.6" stroke="#fff" stroke-width="1.8" fill="none"/></svg>Gated site with round the clock camera cover and alarm</li>
      <li><svg width="16" height="16" viewBox="0 0 16 16"><circle cx="8" cy="8" r="8" fill="#7c1522"/><path d="M4.5 8.3 L7 10.6 L11.6 5.6" stroke="#fff" stroke-width="1.8" fill="none"/></svg>Flexible monthly and yearly plans for every owner</li>
      <li><svg width="16" height="16" viewBox="0 0 16 16"><circle cx="8" cy="8" r="8" fill="#7c1522"/><path d="M4.5 8.3 L7 10.6 L11.6 5.6" stroke="#fff" stroke-width="1.8" fill="none"/></svg>Wash bay and battery charge points</li>
    </ul>
  </section>

  <footer class="contact">
    <div class="contact-line">
      <svg width="16" height="16" viewBox="0 0 24 24"><path d="M6.6 10.8a15 15 0 0 0 6.6 6.6l2.2-2.2a1 1 0 0 1 1-.25 11.4 11.4 0 0 0 3.6.57 1 1 0 0 1 1 1V20a1 1 0 0 1-1 1A17 17 0 0 1 3 4a1 1 0 0 1 1-1h3.5a1 1 0 0 1 1 1c0 1.25.2 2.45.57 3.6a1 1 0 0 1-.25 1z" fill="#ffffff"/></svg>
      <span>0123456789</span>
      <span class="divider">|</span>
      <span>info@companyname.com</span>
    </div>
    <div class="website">www.companyname.com</div>
  </footer>
</main>
</body>
</html>
```